Business card

would like a double sided business card made up with my logos provided.
Prefer card to have black background and to use the black logos, with matching blue writing for the text.
One side to just be the logo, (Try to use both the black logos)
the other side to have the logo and also my credentials/business information.

Covering all aspects of Carpentry and Building Services

Marcus Tolvey
Qualified Carpenter
Mob: 0417263948
Email: rkt.joinery@mailbright.com
ABN: 47 615 209 834

Industry/Entity Type

Business

Contact Information for Business Card

Marcus Tolvey
Qualified Carpenter
Mob: 0417263948
ABN: 47 615 209 834

Requirements
Must have
• Please try to use both the black logos and incorporate into the card.

```html
<!DOCTYPE html>
<html lang="en">
<head>
<meta charset="utf-8">
<title>RKT Joinery – Business Card</title>
<link rel="stylesheet" href="https://fonts.googleapis.com/css2?family=Montserrat:wght@400;600&family=Lato:wght@400;700&family=Open+Sans+Condensed:wght@300&display=swap">
<style>
  :root {
    --page-bg: #8e8e8e;
    --card-black: #0b0b0c;
    --brand-blue: #1f87c7;
    --band-blue: #1c7fbe;
    --ink-white: #f2f2f2;
    --band-white: #f4f4f4;
    --divider: #6d6d6d;
  }
  * { margin: 0; padding: 0; box-sizing: border-box; }
  html, body { width: 1200px; height: 955px; overflow: hidden; }
  body {
    background: var(--page-bg);
    position: relative;
    font-family: "Lato", sans-serif;
  }
  .card {
    position: absolute;
    left: 300px;
    width: 600px;
    height: 343px;
    background: var(--card-black);
    border-radius: 4px;
    overflow: hidden;
    box-shadow: 0 6px 18px rgba(0,0,0,0.35);
  }
  .card--front { top: 95px; }
  .card--back { top: 515px; }

  /* Front */
  .front-brand {
    position: absolute;
    top: 90px; left: 0; width: 100%;
    text-align: center;
  }
  .front-brand .brand-name {
    font-family: "Montserrat", sans-serif;
    font-weight: 600;
    font-size: 56px;
    letter-spacing: 4px;
    color: var(--ink-white);
    line-height: 1;
  }
  .front-brand .brand-trade {
    margin-top: 10px;
    font-family: "Montserrat", sans-serif;
    font-weight: 400;
    font-size: 15px;
    letter-spacing: 6px;
    color: var(--brand-blue);
  }
  .front-tagline {
    position: absolute;
    top: 250px; left: 0; width: 100%;
    text-align: center;
    font-family: "Open Sans Condensed", sans-serif;
    font-weight: 300;
    font-size: 21px;
    color: var(--ink-white);
  }

  /* Back */
  .back-brand {
    position: absolute;
    top: 40px; left: 200px;
  }
  .back-brand .brand-name {
    font-family: "Montserrat", sans-serif;
    font-weight: 600;
    font-size: 32px;
    letter-spacing: 2px;
    color: var(--ink-white);
    line-height: 1;
  }
  .back-brand .brand-trade {
    margin-top: 5px;
    font-family: "Montserrat", sans-serif;
    font-size: 9px;
    letter-spacing: 5px;
    color: var(--brand-blue);
  }
  .holder {
    position: absolute;
    top: 142px; right: 318px;
    text-align: right;
  }
  .holder .holder-name {
    font-weight: 700;
    font-size: 15px;
    color: var(--ink-white);
  }
  .holder .holder-role {
    font-size: 12px;
    color: var(--brand-blue);
    margin-top: 2px;
  }
  .divider {
    position: absolute;
    left: 300px; top: 118px;
    width: 1px; height: 115px;
    background: var(--divider);
  }
  .contact {
    position: absolute;
    top: 160px; left: 318px;
    list-style: none;
  }
  .contact li {
    display: flex;
    align-items: center;
    gap: 8px;
    font-size: 13px;
    color: var(--brand-blue);
    line-height: 19px;
  }
  .contact svg { width: 12px; height: 12px; flex: none; }
  .bands {
    position: absolute;
    left: 0; top: 0;
    width: 600px; height: 343px;
  }
</style>
</head>
<body>

<section class="card card--front" aria-label="Card front">
  <div class="front-brand">
    <div class="brand-name">RKT JOINERY</div>
    <div class="brand-trade">CARPENTERS AND BUILDERS</div>
  </div>
  <p class="front-tagline">Covering all aspects of Carpentry and Building Services</p>
</section>

<section class="card card--back" aria-label="Card back">
  <svg class="bands" viewBox="0 0 600 343" aria-hidden="true">
    <polygon points="0,226 268,226 294,260 0,260" fill="var(--band-blue)"/>
    <polygon points="308,258 600,258 600,300 342,300" fill="var(--band-white)"/>
    <polygon points="342,300 600,300 600,307 347,307" fill="var(--band-blue)"/>
  </svg>

  <div class="back-brand">
    <div class="brand-name">RKT JOINERY</div>
    <div class="brand-trade">CARPENTERS AND BUILDERS</div>
  </div>

  <div class="holder">
    <div class="holder-name">Marcus Tolvey</div>
    <div class="holder-role">Qualified Carpenter</div>
  </div>

  <div class="divider"></div>

  <ul class="contact">
    <li>
      <svg viewBox="0 0 12 12"><rect x="0.5" y="0.5" width="11" height="11" fill="none" stroke="var(--ink-white)"/><rect x="4" y="2" width="4" height="8" rx="0.8" fill="var(--ink-white)"/></svg>
      0417263948
    </li>
    <li>
      <svg viewBox="0 0 12 12"><rect x="0.5" y="0.5" width="11" height="11" fill="none" stroke="var(--ink-white)"/><polygon points="6,2 10,6 9,6 9,10 3,10 3,6 2,6" fill="var(--ink-white)"/></svg>
      ABN: 47 615 209 834
    </li>
    <li>
      <svg viewBox="0 0 12 12"><rect x="0.5" y="0.5" width="11" height="11" fill="none" stroke="var(--ink-white)"/><rect x="2" y="3.5" width="8" height="5" fill="var(--ink-white)"/><polyline points="2,3.5 6,6.5 10,3.5" fill="none" stroke="var(--card-black)" stroke-width="0.8"/></svg>
      rkt.joinery@mailbright.com
    </li>
  </ul>
</section>

</body>
</html>
```